Quillmere Business Advisory Business Card Design Project

I have a new business called Quillmere Business Advisory Limited. We provide business services for the UK for areas which include

Mentoring / Coaching
Interim Management
Non Executive Director / Chairman placement
Angel Investment support
Merger & Acquisition advice
Selling your business advice

I would like a background colour on the logo, a logo and our company name on the logo if possible.

I am open to colours but we want to portray a strong safe business with credibility

The business card design must match that of the logo design

Target Market(s)

SME and Medium size businesses with the owners, MD's, CEO or senior management as the target audiabce

Industry/Entity Type

Business

Requirements
Must have
• Match the logo design.
Look professional and quality
Should not have
• Old style text and colours
Poor logos depicting money

```html
<!DOCTYPE html>
<html lang="en">
<head>
<meta charset="utf-8">
<title>Quillmere Business Advisory – Business Card</title>
<link rel="stylesheet" href="https://fonts.googleapis.com/css2?family=PT+Sans:wght@400;700&display=swap">
<style>
  :root {
    --stage: #a7a7ab;
    --stage-light: #c4c4c8;
    --card-dark: #262626;
    --brand-red: #e63a32;
    --brand-red-deep: #d9322b;
    --ink-light: #ffffff;
    --rule: #d8d8d8;
  }
  * { margin: 0; padding: 0; box-sizing: border-box; }
  html, body { width: 1200px; height: 863px; overflow: hidden; }
  body {
    background: radial-gradient(ellipse at 50% 40%, var(--stage-light), var(--stage) 75%);
    font-family: "PT Sans", sans-serif;
    color: var(--ink-light);
    position: relative;
  }
  .card {
    position: absolute;
    left: 300px;
    width: 600px;
    height: 343px;
    background: var(--card-dark);
    overflow: hidden;
    box-shadow: 0 14px 30px rgba(0,0,0,0.35);
  }
  .card--front { top: 64px; }
  .card--back { top: 456px; }

  .red-panel {
    position: absolute;
    top: 0; bottom: 0;
    background: linear-gradient(135deg, var(--brand-red), var(--brand-red-deep));
  }
  .card--front .red-panel { left: 180px; width: 250px; }
  .card--back .red-panel { left: 330px; right: 0; }

  .wordmark {
    position: absolute;
    left: 0; right: 0;
    text-align: center;
  }
  .wordmark__name {
    display: inline-flex;
    align-items: center;
    gap: 10px;
    font-weight: 400;
    letter-spacing: 1px;
    color: var(--ink-light);
  }
  .wordmark__dot {
    display: inline-block;
    border-radius: 50%;
    background: var(--ink-light);
  }
  .wordmark__tagline {
    display: block;
    font-weight: 700;
    text-transform: uppercase;
    letter-spacing: 1.4px;
    color: var(--ink-light);
  }
  .card--front .wordmark { top: 112px; }
  .card--front .wordmark__name { font-size: 32px; }
  .card--front .wordmark__dot { width: 14px; height: 14px; }
  .card--front .wordmark__tagline { font-size: 7.5px; margin-top: 2px; }
  .card--back .wordmark { top: 135px; }
  .card--back .wordmark__name { font-size: 36px; }
  .card--back .wordmark__dot { width: 16px; height: 16px; }
  .card--back .wordmark__tagline { font-size: 8.5px; margin-top: 2px; }

  .front-web {
    position: absolute;
    left: 14px; bottom: 16px;
    font-size: 13px;
  }

  .contact-list {
    position: absolute;
    left: 30px; top: 24px;
    width: 270px;
    list-style: none;
  }
  .contact-item {
    padding: 6px 0 10px;
    border-bottom: 1.5px solid var(--rule);
    margin-bottom: 12px;
    font-size: 14px;
    line-height: 1.25;
  }
  .contact-item:last-child { margin-bottom: 0; }
  .contact-icon {
    display: block;
    width: 24px; height: 20px;
    margin-bottom: 6px;
    fill: var(--ink-light);
  }
</style>
</head>
<body>

  <section class="card card--front" aria-label="Business card front">
    <div class="red-panel">
      <div class="wordmark">
        <span class="wordmark__name"><span class="wordmark__dot"></span>QUILLMERE</span>
        <span class="wordmark__tagline">Business Advisory Limited</span>
      </div>
      <p class="front-web">www.quillmereadvisory.com</p>
    </div>
  </section>

  <section class="card card--back" aria-label="Business card back">
    <ul class="contact-list">
      <li class="contact-item">
        <svg class="contact-icon" viewBox="0 0 24 20" aria-hidden="true">
          <path d="M12 1 L1 10 H4 V19 H10 V13 H14 V19 H20 V10 H23 Z"/>
        </svg>
        Address Line1, Address Line2,<br>City
      </li>
      <li class="contact-item">
        <svg class="contact-icon" viewBox="0 0 24 20" aria-hidden="true">
          <path d="M2 6 C2 2 22 2 22 6 L19 8 L16 6 V5 H8 V6 L5 8 Z"/>
          <path d="M7 8 H17 L20 18 H4 Z"/>
        </svg>
        000 000 0000<br>000 000 0000
      </li>
      <li class="contact-item">
        <svg class="contact-icon" viewBox="0 0 24 20" aria-hidden="true">
          <path d="M2 1 H22 V14 H2 Z M4 3 V12 H20 V3 Z"/>
          <path d="M10 14 H14 V17 H17 V19 H7 V17 H10 Z"/>
        </svg>
        info@quillmereadvisory.com<br>www.quillmereadvisory.com
      </li>
    </ul>
    <div class="red-panel">
      <div class="wordmark">
        <span class="wordmark__name"><span class="wordmark__dot"></span>QUILLMERE</span>
        <span class="wordmark__tagline">Business Advisory Limited</span>
      </div>
    </div>
  </section>

</body>
</html>
```